RTB sticker for the back window of a car

Well this design is for the back of our car. We want it to be plain and simple but stand out. I have put something together which is a bit to plain and i would like to to look a little bit different. Possibly have a picture of a shipping container on it so people know what we are trying to sell? I don't need our logo on there but i want the phone number and email. Thank you in advance.

Requirements
Must have
• The phone number 0452 317 906 not the one in the picture please.
• Also must have the email that IS in the picture please.
Nice to have
• A picture of a shipping container so people know what we are talking about.

```html
<!DOCTYPE html>
<html lang="en">
<head>
<meta charset="utf-8">
<title>RTB Rear Window Sticker</title>
<link rel="stylesheet" href="https://fonts.googleapis.com/css2?family=Josefin+Sans:wght@700&family=PT+Serif:ital,wght@0,700;1,700&display=swap">
<style>
  :root {
    --maroon: #7a2b2b;
    --sky-edge: #4fc0ee;
    --sky-mid: #a9e2f8;
    --sky-centre: #ffffff;
    --backdrop: #eceae6;
    --photo-sky: #3f78c9;
    --photo-box: #2b4a3e;
    --photo-ground: #8b8f94;
  }
  * { margin: 0; padding: 0; box-sizing: border-box; }
  html, body { width: 1200px; height: 1040px; overflow: hidden; background: var(--backdrop); }
  .canvas { position: relative; width: 1200px; height: 1040px; }
  .sticker-shape { position: absolute; left: 0; top: 0; }
  .headline {
    position: absolute;
    font-family: "Josefin Sans", sans-serif;
    font-weight: 700;
    font-size: 45px;
    line-height: 1;
    color: var(--maroon);
    letter-spacing: -0.5px;
    white-space: nowrap;
  }
  .headline--shipping { left: 278px; top: 364px; }
  .headline--containers { left: 714px; top: 364px; }
  .headline--for-sale { left: 498px; top: 450px; }
  .container-photo { position: absolute; left: 518px; top: 332px; }
  .contact {
    position: absolute;
    top: 530px;
    font-size: 25px;
    line-height: 1;
    color: var(--maroon);
    white-space: nowrap;
  }
  .contact--phone { left: 279px; }
  .contact--email { left: 668px; }
  .contact-label--sans { font-family: "Josefin Sans", sans-serif; font-weight: 700; }
  .contact-label--serif { font-family: "PT Serif", serif; font-weight: 700; }
  .contact-value { font-family: "PT Serif", serif; font-style: italic; font-weight: 700; }
  .brand-name {
    position: absolute;
    top: 594px;
    font-family: "Josefin Sans", sans-serif;
    font-weight: 700;
    font-size: 38px;
    line-height: 1;
    color: var(--maroon);
  }
  .brand-name--left { left: 122px; }
  .brand-name--right { left: 1054px; }
</style>
</head>
<body>
<main class="canvas">
  <svg class="sticker-shape" width="1200" height="1040" viewBox="0 0 1200 1040" aria-hidden="true">
    <defs>
      <radialGradient id="sky-fade" cx="50%" cy="60%" r="60%">
        <stop offset="0" stop-color="var(--sky-centre)"/>
        <stop offset="0.55" stop-color="var(--sky-mid)"/>
        <stop offset="1" stop-color="var(--sky-edge)"/>
      </radialGradient>
    </defs>
    <path d="M182 330 Q630 318 1072 330 L1166 612 Q1170 662 1128 672 Q640 716 134 672 Q96 662 98 612 Z" fill="url(#sky-fade)"/>
  </svg>

  <div class="headline headline--shipping">SHIPPING</div>

  <svg class="container-photo" width="172" height="108" viewBox="0 0 172 108" role="img" aria-label="Photo of a dark green shipping container in a yard under a blue sky">
    <defs>
      <linearGradient id="photo-tones" x1="0" y1="0" x2="0" y2="1">
        <stop offset="0" stop-color="var(--photo-sky)"/>
        <stop offset="0.45" stop-color="var(--photo-box)"/>
        <stop offset="1" stop-color="var(--photo-ground)"/>
      </linearGradient>
    </defs>
    <ellipse cx="86" cy="54" rx="82" ry="50" fill="url(#photo-tones)" stroke="var(--maroon)" stroke-width="5"/>
  </svg>

  <div class="headline headline--containers">CONTAINERS</div>
  <div class="headline headline--for-sale">FOR SALE</div>

  <p class="contact contact--phone"><span class="contact-label--sans">PHONE:</span> <span class="contact-value">0452 317 906</span></p>
  <p class="contact contact--email"><span class="contact-label--serif">EMAIL:</span> <span class="contact-value">sales@rtbcontainers.com.au</span></p>

  <div class="brand-name brand-name--left">RTB</div>
  <div class="brand-name brand-name--right">RTB</div>
</main>
</body>
</html>
```